ebook cover: book 4 in the We Hum Lantern series. Lantern by Riverside

I am wanting a striking cover to bring the forth book in a spiritual journey series to an audience ready to meet new characters and get excited again! White backgrounds, red titles (any font), subtitles to introduce a new major character in the series of ten (same fonts please as the original, We Hum Lantern), and one emblematic, slightly mysterious image. Please keep to the same colour tones as the original, but the lead image need not be gray. Let's please try to use the "light flash" that is on the tin can in We Hum Lantern somehow, in your own way. It is meant to signify the other side, or the higher light, or some such inference.

Book details:
Title: Lantern by Riverside
Subtitle: Archangel Veloriel brings the message
Image: silver hourglass
Author: Maren Tulliver, Ph.D
Strap quote: "Tulliver is smart, savvy and full of ideas," Harbourgate Ledger

Please do your best: this one is going in competition of spiritual healers!

Thanks! :)

```html
<!DOCTYPE html>
<html lang="en">
<head>
<meta charset="utf-8">
<title>Lantern by Riverside — Book Cover</title>
<link href="https://fonts.googleapis.com/css2?family=Bebas+Neue&family=Open+Sans:wght@400;600&display=swap" rel="stylesheet">
<style>
  :root {
    --surround: #000000;
    --paper: #f3f7fa;
    --title-red: #b70d12;
    --title-red-dark: #9c0a0e;
    --ink: #1c1c1c;
    --author-grey: #6a6a6a;
    --glass-light: #eef1f4;
    --glass-mid: #c9ced4;
    --glass-rose: #e8b2b8;
  }
  * { margin: 0; padding: 0; box-sizing: border-box; }
  html, body {
    width: 1200px; height: 1200px; overflow: hidden;
    background: var(--surround);
  }
  .cover {
    position: absolute;
    left: 263px; top: 88px;
    width: 695px; height: 1029px;
    background: var(--paper);
    text-align: center;
  }
  .strap-quote {
    position: absolute; top: 32px; left: 0; right: 0;
    font-family: "Open Sans", sans-serif; font-weight: 600;
    font-size: 11.5px; line-height: 1.7; color: var(--ink);
  }
  .strap-quote .source { font-size: 15px; font-weight: 400; display: block; line-height: 1.3; }
  .book-title {
    position: absolute; top: 100px; left: 0; right: 0;
    font-family: "Bebas Neue", sans-serif; font-weight: 400;
    font-size: 122px; line-height: 108px;
    color: var(--title-red);
    background: linear-gradient(180deg, var(--title-red) 0%, var(--title-red-dark) 100%);
    -webkit-background-clip: text; background-clip: text;
    -webkit-text-fill-color: transparent;
  }
  .book-subtitle {
    position: absolute; top: 326px; left: 0; right: 0;
    font-family: "Open Sans", sans-serif; font-weight: 600;
    font-size: 33px; line-height: 42px; letter-spacing: 0.26em;
    padding-left: 0.26em;
    color: var(--ink);
  }
  .lead-image {
    position: absolute; left: 225px; top: 444px;
    width: 268px; height: 456px;
  }
  .lead-image svg { width: 100%; height: 100%; display: block; }
  .author {
    position: absolute; top: 936px; left: 0; right: 0;
    font-family: "Open Sans", sans-serif; font-weight: 400;
    font-size: 44px; letter-spacing: 0.04em;
    color: var(--author-grey);
  }
  .author .small-cap { font-size: 30px; }
</style>
</head>
<body>
  <main class="cover">
    <p class="strap-quote">"TULLIVER IS SMART, SAVVY AND FULL OF IDEAS"<span class="source">- HARBOURGATE LEDGER</span></p>
    <h1 class="book-title">LANTERN<br>BY RIVERSIDE</h1>
    <h2 class="book-subtitle">ARCHANGEL VELORIEL<br>BRINGS THE MESSAGE</h2>
    <div class="lead-image">
      <svg role="img" aria-label="Silver hourglass with white sand and a rose light flash on the glass" viewBox="0 0 268 456">
        <defs>
          <radialGradient id="glassTone" cx="50%" cy="50%" r="60%">
            <stop offset="0%" stop-color="var(--glass-light)"/>
            <stop offset="70%" stop-color="var(--glass-mid)"/>
            <stop offset="100%" stop-color="var(--paper)" stop-opacity="0"/>
          </radialGradient>
          <radialGradient id="flashTone" cx="78%" cy="40%" r="14%">
            <stop offset="0%" stop-color="var(--glass-rose)" stop-opacity="0.9"/>
            <stop offset="100%" stop-color="var(--glass-rose)" stop-opacity="0"/>
          </radialGradient>
        </defs>
        <rect x="0" y="0" width="268" height="456" rx="30" fill="url(#glassTone)"/>
        <rect x="0" y="0" width="268" height="456" fill="url(#flashTone)"/>
      </svg>
    </div>
    <p class="author">MAREN TULLIVER P<span class="small-cap">H</span>.D.</p>
  </main>
</body>
</html>
```